Simple Business Cards for Self-employed Coach

Simple business card with a design that includes the QLT logo.
Using either only the logo color or additional colors that match the logo.

Meridian Guides reach deeply into the past, gathering wisdom from East and West, while still staying current with the frontiers of new discovery in cognitive science, genetics, and other disciplines. see https://www.brightharborpath.example/what-is-integral-coaching/

Target Market(s)

Coaching Clients in Tokyo /Asia; in business organizations, but also outside

Industry/Entity Type

Life Coaching

Contact Information for Business Card

Lukas Brenning
Certified Meridian Guide

3-2-48 Kamiyoshi
Nakarino 164-0392
Tokyo, Japan

Phone: +81 70 4817 5062
E-Mail: lukas.brenning@mailora.example

Font styles to use
Sans Serif

Colors
00a990

Requirements
Must have
• include uploaded logo
• color fitting with QLT logo color
Nice to have
• simple, elegant design
Should not have
• clutter

```html
<!DOCTYPE html>
<html lang="en">
<head>
<meta charset="utf-8">
<title>QLT Business Card</title>
<link rel="stylesheet" href="https://fonts.googleapis.com/css2?family=Roboto:wght@400;500&display=swap">
<style>
  :root {
    --page-bg: #e9eaea;
    --card-bg: #f7f7f5;
    --teal-deep: #00786a;
    --teal-bright: #00a990;
    --card-shadow: rgba(0, 0, 0, 0.12);
  }
  * { margin: 0; padding: 0; box-sizing: border-box; }
  html, body {
    width: 1200px;
    height: 900px;
    overflow: hidden;
    background: var(--page-bg);
    font-family: "Roboto", Arial, sans-serif;
  }
  .stage {
    width: 1200px;
    height: 900px;
    display: flex;
    align-items: center;
    justify-content: center;
  }
  .business-card {
    width: 920px;
    height: 526px;
    background: var(--card-bg);
    box-shadow: 0 6px 24px var(--card-shadow);
    display: flex;
    align-items: center;
    padding: 0 70px 0 110px;
  }
  .brand {
    width: 340px;
    display: flex;
    align-items: center;
    gap: 18px;
  }
  .brand-square {
    width: 46px;
    height: 46px;
    background: var(--teal-deep);
    flex: none;
  }
  .brand-name {
    font-weight: 500;
    font-size: 72px;
    letter-spacing: 10px;
    color: var(--teal-deep);
    line-height: 1;
  }
  .divider {
    width: 2px;
    height: 150px;
    background: var(--teal-deep);
    margin: 0 44px 0 30px;
    flex: none;
  }
  .contact {
    color: var(--teal-deep);
    font-size: 19px;
    line-height: 1.3;
  }
  .contact-name {
    font-weight: 500;
    font-size: 23px;
  }
  .contact-title {
    color: var(--teal-bright);
    font-size: 20px;
    margin-bottom: 4px;
  }
  .contact-line {
    display: flex;
    align-items: center;
    gap: 10px;
  }
  .contact-icon {
    width: 16px;
    height: 16px;
    flex: none;
  }
  .contact-address { margin-top: 2px; }
</style>
</head>
<body>
  <main class="stage">
    <section class="business-card">
      <div class="brand">
        <span class="brand-square"></span>
        <span class="brand-name">QLT</span>
      </div>
      <span class="divider"></span>
      <div class="contact">
        <p class="contact-name">Lukas Brenning</p>
        <p class="contact-title">Certified Meridian Guide</p>
        <p class="contact-line">
          <svg class="contact-icon" viewBox="0 0 24 24" aria-hidden="true">
            <path fill="#00a990" d="M6.6 10.8a15.1 15.1 0 0 0 6.6 6.6l2.2-2.2c.3-.3.7-.4 1-.2 1.1.4 2.3.6 3.6.6.6 0 1 .4 1 1V20c0 .6-.4 1-1 1C10.6 21 3 13.4 3 4c0-.6.4-1 1-1h3.5c.6 0 1 .4 1 1 0 1.3.2 2.5.6 3.6.1.3 0 .7-.2 1z"/>
          </svg>
          <span>+81 70 4817 5062</span>
        </p>
        <p class="contact-line">
          <svg class="contact-icon" viewBox="0 0 24 24" aria-hidden="true">
            <rect x="2" y="5" width="20" height="14" rx="1.5" fill="#00a990"/>
            <path d="M3 6l9 7 9-7" fill="none" stroke="#f7f7f5" stroke-width="1.8"/>
          </svg>
          <span>lukas.brenning@mailora.example</span>
        </p>
        <p class="contact-address">3-2-48 Kamiyoshi<br>Nakarino 164-0392, Tokyo, Japan</p>
      </div>
    </section>
  </main>
</body>
</html>
```